Wren Vehicle Polishing (Mobile detail)

I need a business card made up. I'd like it to be different in some form, either raised, embossed, debossed, something cool that stands out. (preferably embossed text somewhere in it). I will be including the Initial png file. Let me know if you need the photoshop of adobe illustrator file to work with.
Updates

Information to be included: Text: XXX-XXX-XXXX Phone: XXX-XXX-XXXX Email: wrenvehiclepolish@mailnest.example Website: www.socialpage.example/wrenvehiclepolishKTR Hours of operation: Mon - Fri 7:00AM to 8:00PM Sat - 10:00AM to 8:00PM

Target Market(s)

Mobile automotive detailing

Industry/Entity Type

Automotive

Contact Information for Business Card

Make it stand out with embossed lettering, I'd also like the background to be glossy black or matte, something that represents a shiny car, black preferred

Requirements
Must have
• A glossy background, or something.
• My logo, pick one of them that best fits your design.
Should not have
• White background,
• something that does not stand out.

```html
<!DOCTYPE html>
<html lang="en">
<head>
<meta charset="utf-8">
<title>Wren Vehicle Polishing – Business Card</title>
<link href="https://fonts.googleapis.com/css2?family=Libre+Baskerville:wght@700&family=Roboto:wght@400;500&display=swap" rel="stylesheet">
<style>
  :root {
    --page-bg: #2b2724;
    --card-black: #050505;
    --card-sheen: #2a2a2a;
    --accent-orange: #f07f2a;
    --text-light: #e9e9e9;
    --text-muted: #cfcfcf;
    --divider: #8a8a8a;
  }
  * { margin: 0; padding: 0; box-sizing: border-box; }
  html, body {
    width: 1200px;
    height: 1022px;
    overflow: hidden;
    background: var(--page-bg);
  }
  .canvas {
    width: 1200px;
    height: 1022px;
    display: flex;
    align-items: center;
    justify-content: center;
  }
  .business-card {
    position: relative;
    width: 1000px;
    height: 572px;
    border-radius: 26px;
    overflow: hidden;
    background:
      linear-gradient(115deg, transparent 30%, rgba(255,255,255,0.10) 42%, rgba(255,255,255,0.03) 55%, transparent 62%),
      radial-gradient(ellipse at 40% 45%, var(--card-sheen) 0%, var(--card-black) 65%);
    box-shadow: 0 20px 50px rgba(0,0,0,0.55);
    font-family: "Roboto", Arial, sans-serif;
    color: var(--text-light);
  }
  .hours {
    position: absolute;
    top: 44px;
    left: 60px;
    font-size: 25px;
    letter-spacing: 0.2px;
    color: var(--text-light);
  }
  .hours-label { color: var(--accent-orange); }

  .brand {
    position: absolute;
    left: 80px;
    top: 200px;
    width: 380px;
    display: flex;
    align-items: center;
    gap: 20px;
  }
  .brand-dot {
    flex: none;
    width: 46px;
    height: 46px;
    border-radius: 50%;
    background: var(--accent-orange);
  }
  .brand-name {
    font-family: "Roboto", Arial, sans-serif;
    font-weight: 500;
    font-size: 42px;
    line-height: 1.12;
    color: var(--text-light);
  }

  .divider {
    position: absolute;
    left: 490px;
    top: 150px;
    width: 2px;
    height: 330px;
    background: linear-gradient(to bottom, transparent, var(--divider) 20%, var(--divider) 80%, transparent);
    transform: rotate(12deg);
  }

  .contact {
    position: absolute;
    left: 560px;
    top: 150px;
    width: 420px;
  }
  .person-name {
    font-family: "Libre Baskerville", Georgia, serif;
    font-weight: 700;
    font-size: 36px;
    color: var(--accent-orange);
    letter-spacing: 0.5px;
  }
  .person-role {
    margin-top: 6px;
    font-size: 23px;
    color: var(--text-light);
  }
  .contact-list {
    list-style: none;
    margin-top: 34px;
  }
  .contact-item {
    display: flex;
    align-items: center;
    gap: 14px;
    font-size: 22px;
    line-height: 1.55;
    color: var(--text-muted);
    white-space: nowrap;
  }
  .contact-item.long { font-size: 17px; }
  .contact-icon {
    flex: none;
    width: 20px;
    height: 20px;
  }
</style>
</head>
<body>
<main class="canvas">
  <section class="business-card">
    <p class="hours"><span class="hours-label">Hours of operation:</span> Mon - Fri 7:00AM to 8:00PM Sat - 10:00AM to 8:00PM</p>

    <div class="brand">
      <span class="brand-dot"></span>
      <span class="brand-name">Wren Vehicle Polishing</span>
    </div>

    <div class="divider"></div>

    <div class="contact">
      <h1 class="person-name">MARLO KEATING</h1>
      <p class="person-role">DIRECTOR</p>
      <ul class="contact-list">
        <li class="contact-item">
          <svg class="contact-icon" viewBox="0 0 20 20" aria-hidden="true"><rect x="5" y="1.5" width="10" height="17" rx="2" fill="none" stroke="#f07f2a" stroke-width="2"/><circle cx="10" cy="15" r="1.2" fill="#f07f2a"/></svg>
          XXX-XXX-XXXX
        </li>
        <li class="contact-item">
          <svg class="contact-icon" viewBox="0 0 20 20" aria-hidden="true"><path d="M5 2 L8 6 L6.5 8 Q8.5 12 12 13.5 L14 12 L18 15 L16 18 Q9 18 5 12 Q2 7 5 2 Z" fill="#f07f2a"/></svg>
          XXX-XXX-XXXX
        </li>
        <li class="contact-item long">
          <svg class="contact-icon" viewBox="0 0 20 20" aria-hidden="true"><rect x="2" y="4" width="16" height="12" fill="none" stroke="#f07f2a" stroke-width="2"/><path d="M2 4 L10 11 L18 4" fill="none" stroke="#f07f2a" stroke-width="2"/></svg>
          wrenvehiclepolish@mailnest.example
        </li>
        <li class="contact-item long">
          <svg class="contact-icon" viewBox="0 0 20 20" aria-hidden="true"><circle cx="10" cy="10" r="5" fill="#f07f2a"/></svg>
          www.socialpage.example/wrenvehiclepolishKTR
        </li>
      </ul>
    </div>
  </section>
</main>
</body>
</html>
```